依頼詳細
シンプルかつスタイリッシュで、落ち着いたデザインを希望します。弊社イメージカラーはオレンジですが、建物との統一性を持たせたカラー(紺色:写真参照)のほうが良いかと思っています。(オレンジを使用していただいても結構です)
サイズや表記内容等は「記載項目」をご覧ください。
記載項目
ミナセリアルティ株式会社
ミナセリーガル事務所またはミナセリーガル行政書士|土地家屋調査士事務所(バランス等考慮し、どちらかを選択)は必須ですが、電話番号は必要ありません。
また、ロゴマークも必須ですが、マークの選択はお任せします。(添付ファイル参照)
また、事業内容については参考に名刺を添付しますが、多くの情報を入れることは望みません。事業所名をミナセリーガル事務所とする場合は、行政書士及び土地家屋調査士を事業内容としていただいても結構です。
寸法につきましては、添付ファイルをご確認ください。

希望イメージ
シンプル 複雑
単色 カラフル
暗い 明るい
日常 高級
遊び心 厳粛
未来的 伝統的
女性的 男性的
希望する色
事務所看板のため、建物と統一性のあるものにしたいです
納品ファイル
• イラストレーター形式 (.ai)
補足説明
事業内容は必ずしも記載しなければならないものではありません。(どちらでもよいです)
■ 選んだ理由

「シンプルでスタイリッシュ」の希望を見事に叶えていただきました。
中でもロゴの配置が絶妙で、色合いも素晴らしかったです。

■ 提案者全員のお礼・コメント

この度は弊社コンペにご参加いただきまして、誠にありがとうございました。
レベルが高く秀逸な作品が多いため選定に悩みましたが、嬉しい悲鳴で選定を楽しませていただきました。
今後も業務拡大を目指しておりますので、折に触れコンペを開催させていただくつもりですので、引き続きよろしくお願いいたします。

```html
<!DOCTYPE html>
<html lang="ja">
<head>
<meta charset="utf-8">
<title>ミナセリーガル事務所 看板</title>
<link rel="stylesheet" href="https://fonts.googleapis.com/css2?family=Noto+Sans+JP:wght@500;700&family=Noto+Serif:wght@400&display=swap">
<style>
  :root {
    --page: #ffffff;
    --navy: #27313f;
    --orange: #e8751f;
    --text-light: #ffffff;
    --text-dark: #1c1c1c;
  }
  * { margin: 0; padding: 0; box-sizing: border-box; }
  html, body {
    width: 849px; height: 1200px; overflow: hidden;
    background: var(--page);
  }
  .sign {
    position: absolute; left: 232px; top: 65px;
    width: 388px; height: 1039px;
    background: var(--navy);
    color: var(--text-light);
    font-family: "Noto Sans JP", sans-serif;
  }
  .brand {
    position: absolute; top: 150px; left: 0; width: 100%;
    display: flex; flex-direction: column; align-items: center;
  }
  .brand-dot {
    width: 64px; height: 64px; border-radius: 50%;
    background: var(--orange);
  }
  .brand-name {
    margin-top: 62px;
    font-family: "Noto Serif", serif;
    font-size: 25px; letter-spacing: 1px;
    color: var(--text-light);
  }
  .office-name {
    position: absolute; top: 370px; left: 0; width: 100%;
    text-align: center; font-weight: 700; font-size: 29px;
    letter-spacing: 0.5px;
  }
  .services {
    position: absolute; top: 498px; left: 43px; width: 302px;
    list-style: none;
  }
  .service {
    text-align: center; font-weight: 500; font-size: 22px;
    padding-bottom: 8px; margin-bottom: 28px;
    border-bottom: 2px solid var(--orange);
  }
  .company-band {
    position: absolute; left: 0; bottom: 0;
    width: 100%; height: 147px;
    background: var(--orange);
    color: var(--text-dark);
    font-weight: 700; font-size: 26px;
    text-align: center; padding-top: 28px;
    letter-spacing: 0.5px;
  }
</style>
</head>
<body>
  <div class="sign">
    <div class="brand">
      <div class="brand-dot"></div>
      <div class="brand-name">MINASE REALTY</div>
    </div>
    <h1 class="office-name">ミナセリーガル事務所</h1>
    <ul class="services">
      <li class="service">行政書士</li>
      <li class="service">土地家屋調査士</li>
    </ul>
    <div class="company-band">ミナセリアルティ株式会社</div>
  </div>
</body>
</html>
```